HVRT LLP website - revamping our website after 23 years

Our website needs a complete overhaul. The purpose of this exercise is to provide us with your vision of what you think the website should look like. We don't need the website to be created or coded. Just need creative designs.

We have a four sites that we would like to base our website on;

We like the simplicity of Ravelstoke, the style of Pemberly Adair and Quillfeather.

http://www.pemberlyadair.example/en/toronto-ontario/
http://www.ravelstoke.example/
vintquillfeather.example
http://www.brindlemoor.example/our-professionals.html

We have a logo that we would like to use which will be attached below. We need to keep our website looking very professional as we have a large number of high net worth clients.
Updates

Hi, We've received some good website designs but they appear to be the same type of template websites we've received in the past - this is not what we're looking for. What we want is a unique website that is modelled on the following three company websites: http://www.ravelstoke.example/ www.vintquillfeather.example/ http://www.pemberlyadair.example/en/toronto-ontario/

Thank you everyone for your designs. I will be posting updates and my comments on the various designs in the next day - I want to thank you for the creative designs I see. I thought i would explain a bit about our firm and perhaps it can help when you design the theme of our website: - Our firm is like a family and our clients are truly like our friends. We have close knit relationships in and outside of the office with staff and clients. - We are an 'out of the box' type of firm. We operate differently than most firms and that's a differentiating factor in what makes us who we are - Our slogan is "Count on us" which is a testament to the way we run our practice - We would like an open, fresh, clean look to our website - we don't want the landing page to be overly long or complex because we have limited time to update the website and limited content That's it for the time being - when things come to mind I will post them here.

Can we try a design as follows: - make the website look very similar to www.ravelstoke.example - use the same background colour - Keep the same black top but insert our logo - incorporate some of the content from our current website www.hvrt-ca.example

I have been away dealing with a personal matter. I will look into these websites tomorrow afternoon and provide more feedback / info on the top designer. Thank you

Hi designers, I want to apologize for the delay. I plan on wrapping things up within the next few days. I will go through a few of the top designs and offer my comments. Thank you for your patience.

Target Market(s)

Mainly our current clients - We have a large number of high net worth individuals as clients.

Industry/Entity Type

Accounting

Number of Pages Required

1 page

Requirements
Must have
• Please model website on the websites indicated above.
• Our current website is www.hvrt-ca.example. It's dark, cluttered and not inviting. We want a fresh, clean website. Please incorporate the logo's attached below.

```html
<!DOCTYPE html>
<html lang="en">
<head>
<meta charset="utf-8">
<title>HVRT LLP — Chartered Professional Accountants</title>
<link rel="stylesheet" href="https://fonts.googleapis.com/css2?family=Open+Sans:ital,wght@0,400;0,600;0,700;1,400&display=swap">
<style>
:root{
  --dark:#2f3032;
  --darker:#232426;
  --footer:#333436;
  --green:#8dc63f;
  --purple:#6a2c8e;
  --magenta:#a21d5e;
  --blue:#27a8df;
  --text:#555;
  --heading:#222;
  --light:#fff;
  --muted:#aaa;
}
*{box-sizing:border-box;margin:0;padding:0}
html,body{width:1200px;height:3130px;overflow:hidden}
body{font-family:"Open Sans",Arial,sans-serif;color:var(--text);background:#fff;position:relative}
.abs{position:absolute}

/* header */
.site-header{position:absolute;left:0;top:0;width:1200px;height:125px;background:var(--dark)}
.brand{position:absolute;left:112px;top:36px;display:flex;align-items:center;gap:12px;color:var(--light);font-size:30px;font-weight:400;letter-spacing:.5px}
.brand-mark{width:30px;height:30px;background:var(--magenta)}
.contact-bar{position:absolute;right:60px;top:28px;display:flex;gap:36px;font-size:13px;color:#ccc}
.contact-bar span{display:flex;align-items:center;gap:10px}
.dot{width:28px;height:28px;border-radius:50%;display:inline-flex;align-items:center;justify-content:center}
.main-nav{position:absolute;right:48px;top:86px;display:flex;gap:42px;font-size:12.5px;font-weight:700;color:var(--light);letter-spacing:.3px}

/* hero */
.hero{position:absolute;left:0;top:125px;width:1200px;height:493px;background:linear-gradient(100deg,#e9eef2 0%,#c9d3db 30%,#5c6670 60%,#2b2f36 85%,#7b8a97 100%)}
.hero-title{position:absolute;left:98px;top:157px;font-size:42px;font-weight:700;color:var(--blue)}
.hero-sub{position:absolute;left:98px;top:214px;font-size:22px;font-weight:700;color:#222;line-height:30px}
.btn{display:inline-block;background:var(--green);color:var(--light);font-size:12.5px;font-weight:700;text-align:center}
.hero .btn{position:absolute;left:98px;top:288px;width:170px;height:42px;line-height:42px}

/* tiles */
.tiles{position:absolute;left:0;top:618px;width:1200px;height:286px;display:flex}
.tile{width:300px;height:286px;color:var(--light);text-align:center;padding-top:44px}
.tile svg{display:block;margin:0 auto 22px}
.tile h3{font-size:15px;font-weight:700;margin-bottom:18px;letter-spacing:.3px}
.tile p{font-size:11.5px;line-height:22px;width:200px;margin:0 auto}
.tile-green{background:var(--green)}.tile-purple{background:var(--purple)}
.tile-magenta{background:var(--magenta)}.tile-blue{background:var(--blue)}

/* sections */
.section-title{position:absolute;left:0;width:1200px;text-align:center;font-size:20px;font-weight:700;color:var(--heading)}
.section-intro{position:absolute;left:200px;width:800px;text-align:center;font-size:14px;line-height:30px;color:#666}

.service{position:absolute;width:313px;text-align:center}
.service .photo{width:313px;height:192px}
.service h4{font-size:12px;font-weight:700;color:var(--heading);margin:28px 0 14px}
.service p{font-size:11.5px;line-height:22px;color:#555;padding:0 14px}
.services-more{position:absolute;left:507px;top:1895px;width:186px;height:46px;line-height:46px}

.touch{position:absolute;display:flex;gap:36px;width:440px}
.touch h5{font-size:12px;font-weight:700;color:var(--heading);margin-bottom:10px}
.touch p{font-size:11.5px;line-height:22px;color:#555}

/* testimonials */
.testimonials{position:absolute;left:0;top:2452px;width:1200px;height:376px;background:linear-gradient(100deg,#3a3d42 0%,#585b60 40%,#4a4d52 70%,#2e3034 100%)}
.testimonials h2{position:absolute;left:0;top:56px;width:1200px;text-align:center;color:var(--light);font-size:21px;font-weight:700}
.quote{position:absolute;left:280px;top:108px;width:640px;text-align:center;color:#eee;font-size:13px;line-height:26px}
.qmark{position:absolute;color:#eee;font-size:40px;font-family:Georgia,serif}
.avatar{position:absolute;left:468px;top:224px;width:84px;height:84px;border-radius:50%;background:#d8d8d8;border:3px solid #fff}
.person{position:absolute;left:572px;top:240px;color:#fff;font-size:13px;line-height:24px}
.person em{font-size:13px}
.arrow{position:absolute;top:170px;color:#aaa;font-size:26px}

/* footer */
.site-footer{position:absolute;left:0;top:2828px;width:1200px;height:250px;background:var(--footer);color:#bbb;font-size:11.5px}
.fcol{position:absolute;top:40px;line-height:21px}
.fcol h6{font-size:12px;font-weight:700;color:#fff;margin-bottom:10px}
.fbrand{position:absolute;left:955px;top:110px;display:flex;align-items:center;gap:10px;color:#fff;font-size:26px}
.bottom-bar{position:absolute;left:0;top:3078px;width:1200px;height:52px;background:var(--darker);color:#aaa;font-size:11px;line-height:52px}
.bottom-bar .legal{position:absolute;left:100px}
.bottom-bar .legal span{margin-right:24px}
.socials{position:absolute;right:72px;top:20px;display:flex;gap:26px}
.socials i{width:11px;height:11px;border-radius:50%;background:#888;display:block}
</style>
</head>
<body>

<header class="site-header">
  <div class="brand"><span class="brand-mark"></span>HVRT LLP</div>
  <div class="contact-bar">
    <span><i class="dot" style="background:var(--green)"><svg width="14" height="14" viewBox="0 0 24 24"><path d="M6 2l4 4-2 3c1 3 4 6 7 7l3-2 4 4-3 4C10 21 3 14 2 5z" fill="#fff"/></svg></i>Tel: (416) 555-0140</span>
    <span><i class="dot" style="background:var(--blue)"><svg width="14" height="14" viewBox="0 0 24 24"><path d="M6 2l4 4-2 3c1 3 4 6 7 7l3-2 4 4-3 4C10 21 3 14 2 5z" fill="#fff"/></svg></i>Fax: (416) 555-0141</span>
    <span><i class="dot" style="background:var(--magenta)"><svg width="14" height="12" viewBox="0 0 24 20"><rect x="1" y="2" width="22" height="16" fill="none" stroke="#fff" stroke-width="2"/><path d="M1 2l11 9 11-9" fill="none" stroke="#fff" stroke-width="2"/></svg></i>Email: info@hvrt-ca.example</span>
  </div>
  <nav class="main-nav"><span>HOME</span><span>ABOUT HVRT</span><span>SERVICES</span><span>LIBRARY</span><span>LINKS</span><span>CAREERS</span><span>CONTACT US</span></nav>
</header>

<section class="hero" role="img" aria-label="Photo of three businessmen in suits shaking hands in a bright glass office building">
  <h1 class="hero-title">HVRT LLP</h1>
  <p class="hero-sub">CHARTERED PROFESSIONAL<br>ACCOUNTANTS</p>
  <span class="btn">VIEW OUR HISTORY</span>
</section>

<section class="tiles">
  <div class="tile tile-green">
    <svg width="70" height="56" viewBox="0 0 70 56" fill="none" stroke="#fff" stroke-width="2"><circle cx="26" cy="16" r="11"/><path d="M4 52c0-14 10-22 22-22s22 8 22 22z"/><circle cx="46" cy="14" r="9"/><path d="M46 28c10 0 20 6 20 20H52"/></svg>
    <h3>WHO WE ARE</h3><p>At its core, Halden Analytics is an innovative technical company with a history of solving challenging problems for a variety</p>
  </div>
  <div class="tile tile-purple">
    <svg width="60" height="56" viewBox="0 0 60 56" fill="none" stroke="#fff" stroke-width="2"><path d="M26 8A22 22 0 1 0 48 30H26z"/><path d="M32 3v21h21A21 21 0 0 0 32 3z"/></svg>
    <h3>WHY WE ARE DIFFERENT</h3><p>At its core, Halden Analytics is an innovative technical company with a history of solving challenging problems for a variety</p>
  </div>
  <div class="tile tile-magenta">
    <svg width="66" height="56" viewBox="0 0 66 56" fill="none" stroke="#fff" stroke-width="2"><rect x="6" y="32" width="10" height="20"/><rect x="22" y="22" width="10" height="30"/><rect x="38" y="28" width="10" height="24"/><rect x="54" y="12" width="10" height="40"/><path d="M4 22l16-12 14 8 16-14"/></svg>
    <h3>PARTNER INFORMATION</h3><p>At its core, Halden Analytics is an innovative technical company with a history of solving challenging problems for a variety</p>
  </div>
  <div class="tile tile-blue">
    <svg width="56" height="56" viewBox="0 0 56 56" fill="none" stroke="#fff" stroke-width="2"><circle cx="28" cy="16" r="13"/><path d="M4 54c0-14 10-24 24-24s24 10 24 24z"/></svg>
    <h3>STAFF PROFILES</h3><p>At its core, Halden Analytics is an innovative technical company with a history of solving challenging problems for a variety</p>
  </div>
</section>

<h2 class="section-title" style="top:962px">HVRT SERVICES</h2>
<p class="section-intro" style="top:998px">HVRT, Harwood Vance Reinholt Tate LLP Chartered Accountants, is a full-service, public accounting firm, primarily serving the small and mid-size, entrepreneurial business and professional sectors in Toronto Canada.</p>

<div class="service" style="left:98px;top:1112px"><div class="photo" role="img" aria-label="Photo of an accountant working with a calculator and papers" style="background:linear-gradient(135deg,#e6e2de,#9a8e86)"></div><h4>ACCOUNTING AND AUDITING</h4><p>Accounting and auditing are the bread and butter of the traditional accounting practice. At HVRT we understand, however, that these roles are only a small part of our overall client service. The watchword is value or value added.</p></div>
<div class="service" style="left:445px;top:1112px"><div class="photo" role="img" aria-label="Photo of business people in a meeting" style="background:linear-gradient(135deg,#c7d4e2,#6f7f90)"></div><h4>BUSINESS ADVISORY</h4><p>Accounting and auditing are the bread and butter of the traditional accounting practice. At HVRT we understand, however, that these roles are only a small part of our overall client service. The watchword is value or value added.</p></div>
<div class="service" style="left:791px;top:1112px"><div class="photo" role="img" aria-label="Photo of a figure standing on top of a tall column against a blue sky" style="background:linear-gradient(180deg,#1c4f8f,#7fb0dd)"></div><h4>DUE DILIGENCE</h4><p>Accounting and auditing are the bread and butter of the traditional accounting practice. At HVRT we understand, however, that these roles are only a small part of our overall client service. The watchword is value or value added.</p></div>

<div class="service" style="left:98px;top:1507px"><div class="photo" role="img" aria-label="Photo of glass office towers" style="background:linear-gradient(180deg,#b9cbd9,#3e5365)"></div><h4>HIGH-TECH INDUSTRY</h4><p>Accounting and auditing are the bread and butter of the traditional accounting practice. At HVRT we understand, however, that these roles are only a small part of our overall client service. The watchword is value or value added.</p></div>
<div class="service" style="left:445px;top:1507px"><div class="photo" role="img" aria-label="Photo of businessmen talking on the phone" style="background:linear-gradient(135deg,#dfe6ee,#485566)"></div><h4>INVESTORS AND WEALTH MANAGEMENT</h4><p>Accounting and auditing are the bread and butter of the traditional accounting practice. At HVRT we understand, however, that these roles are only a small part of our overall client service. The watchword is value or value added.</p></div>
<div class="service" style="left:791px;top:1507px"><div class="photo" role="img" aria-label="Photo of a doctor holding a stethoscope" style="background:linear-gradient(135deg,#f2f2f2,#c9d6de)"></div><h4>MEDICAL PROFESSIONALS</h4><p>Accounting and auditing are the bread and butter of the traditional accounting practice. At HVRT we understand, however, that these roles are only a small part of our overall client service. The watchword is value or value added.</p></div>

<span class="btn services-more">VIEW MORE SERVICES</span>

<h2 class="section-title" style="top:1996px">GET IN TOUCH</h2>
<p class="section-intro" style="top:2042px">HVRT, Harwood Vance Reinholt Tate LLP Chartered Accountants, is a full-service, public accounting firm, primarily serving the small and mid-size, entrepreneurial business and professional sectors in Toronto Canada.</p>

<div class="touch" style="left:142px;top:2139px">
  <svg width="46" height="44" viewBox="0 0 46 44" fill="none" stroke="#444" stroke-width="1.8"><path d="M2 2h42v28H18l-10 10v-10H2z"/><path d="M10 12h26M10 20h18"/></svg>
  <div><h5>FEEDBACK</h5><p>Our dashboard allows operators and users of the system to review, configure, and manage information from remote and local assets.</p></div>
</div>
<div class="touch" style="left:645px;top:2139px">
  <svg width="46" height="44" viewBox="0 0 46 44" fill="none" stroke="#444" stroke-width="1.8"><path d="M2 12l12-5 18 5 12-5v30l-12 5-18-5-12 5z"/><path d="M23 30c-6-7-8-11-8-14a8 8 0 0 1 16 0c0 3-2 7-8 14z" fill="#fff"/><circle cx="23" cy="16" r="3"/></svg>
  <div><h5>DIRECTIONS</h5><p>Our platform utilizes the same network as mission critical military and infrastructure systems and has a proven track record.</p></div>
</div>
<div class="touch" style="left:142px;top:2283px">
  <svg width="46" height="46" viewBox="0 0 46 46" fill="none" stroke="#444" stroke-width="1.8"><circle cx="23" cy="23" r="21"/><path d="M23 10v13l9 6"/></svg>
  <div><h5>HOURS OF OPERATION</h5><p>Unlike traditional monitoring systems our platform utilizes one or more satellite networks we can ensure consistent quality of service across the globe.</p></div>
</div>
<div class="touch" style="left:645px;top:2283px">
  <svg width="46" height="46" viewBox="0 0 24 24" fill="none" stroke="#444" stroke-width="1"><path d="M6 2l4 4-2 3c1 3 4 6 7 7l3-2 4 4-3 4C10 21 3 14 2 5z"/></svg>
  <div><h5>CONTACT AN INDIVIDUAL</h5><p>Halden Analytics has solved the critical power harvesting and management issues, our low power systems have a full integrated control system.</p></div>
</div>

<section class="testimonials" role="img" aria-label="Blurred photo of a laptop on a desk behind the testimonial">
  <h2>TESTIMONIALS</h2>
  <span class="qmark" style="left:232px;top:84px">&ldquo;</span>
  <p class="quote">Es simplemente el texto de relleno de las imprentas y archivos de texto. Lorem ipsum ha sido el texto de relleno estándar de las industrias desde el año 1500, cuando un impresor (N. del T. persona que se dedica a la imprenta) desconocido usó una galería de textos y los mezcló de tal manera</p>
  <span class="qmark" style="left:942px;top:160px">&rdquo;</span>
  <span class="arrow" style="left:142px">&lsaquo;</span>
  <span class="arrow" style="left:1034px">&rsaquo;</span>
  <div class="avatar" role="img" aria-label="Client portrait photo"></div>
  <div class="person">Marcus Ellery<br><em>Business man</em></div>
</section>

<footer class="site-footer">
  <div class="fcol" style="left:100px"><h6>WELCOME</h6>Home<br>About HVRT<br>Services<br>Library<br>Links<br>Careers<br>Contact Us</div>
  <div class="fcol" style="left:248px"><h6>SERVICES</h6>Accounting and Auditing<br>Business Advisory<br>Due Diligence<br>High-Tech Industry<br>Investors and Wealth Management<br>Medical Professionals</div>
  <div class="fcol" style="left:478px"><h6>&nbsp;</h6>Not for Profit and Charitable Sector<br>Personal Tax Services<br>The Legal Profession<br>The Real Estate Industry<br>Tax Planning and Compliance</div>
  <div class="fcol" style="left:743px"><h6>CONTACT US</h6>Suite 1204, 880 Alder Street<br>Toronto, Ontario<br>Canada, M5V 2T3<br><br>Tel: (416) 555-0140<br>Fax: (416) 555-0141<br>Email: info@hvrt-ca.example</div>
  <div class="fbrand"><span class="brand-mark"></span>HVRT LLP</div>
</footer>
<div class="bottom-bar">
  <div class="legal"><span>© 2015, HVRT. All rights reserved.</span><span>Terms of Service</span><span>/</span><span>Privacy Policy</span></div>
  <div class="socials"><i></i><i></i><i></i><i></i><i></i><i></i></div>
</div>

</body>
</html>
```